Delbert n Db Lawn Care needs a vehicle wrap design

We need a vehicle wrap for a pickup truck. This is for a lawn care service. The business is located in florida.

```html
<!DOCTYPE html>
<html lang="en">
<head>
<meta charset="utf-8">
<title>Delbert n Db Lawn Care – Vehicle Wrap</title>
<link rel="stylesheet" href="https://fonts.googleapis.com/css2?family=Black+Ops+One&family=Russo+One&family=Teko:wght@600&display=swap">
<style>
  :root {
    --bg: #efefef;
    --wrap-white: #f4f4f4;
    --wrap-grey: #dcdcdc;
    --green-dark: #1f7a1c;
    --green-main: #2f9a22;
    --green-light: #8cc63f;
    --lime: #b5dc5a;
    --ink: #1a1a1a;
    --white: #ffffff;
    --mascot-red: #c8202a;
  }
  * { box-sizing: border-box; margin: 0; padding: 0; }
  html, body { width: 1200px; height: 525px; overflow: hidden; background: var(--bg); }
  .canvas { position: relative; width: 1200px; height: 525px; }

  .wrap-panel { position: absolute; left: 85px; top: 127px; width: 1040px; height: 262px;
    border-radius: 18px; overflow: hidden; background: linear-gradient(180deg, var(--white), var(--wrap-grey)); }
  .wrap-shapes { position: absolute; inset: 0; z-index: 0; }

  .grass { position: absolute; left: 235px; bottom: 0; width: 805px; height: 34px; z-index: 1;
    background: linear-gradient(180deg, rgba(140,198,63,0) 0%, var(--green-light) 45%, var(--green-main) 100%); }

  .service-headline { position: absolute; left: 62px; top: 112px; z-index: 2;
    font-family: "Russo One", sans-serif; color: var(--green-dark); transform: rotate(-2deg); transform-origin: left; }
  .service-headline .main { font-size: 23px; line-height: 1; letter-spacing: 0.5px; }
  .service-headline .sub { font-size: 11px; margin-top: 4px; }

  .mascot { position: absolute; left: 250px; top: 92px; width: 140px; height: 130px; border-radius: 14px; z-index: 2;
    background: radial-gradient(circle at 50% 45%, var(--mascot-red), #7a1a1a 70%, #444); }

  .company-name { position: absolute; left: 403px; top: 118px; z-index: 2;
    font-family: "Black Ops One", sans-serif; font-weight: 400; font-size: 25px; line-height: 31px; color: var(--ink);
    text-transform: uppercase; letter-spacing: 1px; text-shadow: 0 0 3px var(--white), 0 0 3px var(--white); }

  .phone { position: absolute; left: 680px; top: 72px; z-index: 2;
    font-family: "Teko", sans-serif; font-weight: 600; font-size: 64px; line-height: 1; color: var(--white);
    letter-spacing: 1px;
    text-shadow: -1.5px -1.5px 0 var(--green-dark), 1.5px -1.5px 0 var(--green-dark), -1.5px 1.5px 0 var(--green-dark), 1.5px 1.5px 0 var(--green-dark), 4px 4px 0 var(--ink); }
  .tagline { position: absolute; left: 672px; top: 138px; z-index: 2;
    font-family: "Russo One", sans-serif; font-size: 13.5px; color: var(--white); letter-spacing: 0.4px; transform: rotate(-1deg); }
</style>
</head>
<body>
<main class="canvas">
  <section class="wrap-panel">
    <svg class="wrap-shapes" viewBox="0 0 1040 262" preserveAspectRatio="none" aria-hidden="true">
      <path d="M640 0 Q720 120 650 262 L1040 262 L1040 0 Z" fill="var(--lime)"/>
      <path d="M665 0 Q745 120 675 262 L1040 262 L1040 0 Z" fill="var(--green-light)"/>
      <path d="M690 0 Q770 120 700 262 L1040 262 L1040 0 Z" fill="var(--green-main)"/>
      <path d="M940 0 L1040 0 L1040 262 L980 262 Q1040 130 940 0 Z" fill="var(--green-dark)" opacity="0.35"/>
    </svg>

    <div class="grass" role="img" aria-label="Illustrated green grass blades along the bottom edge"></div>

    <div class="service-headline">
      <div class="main">CUT AND EDGE</div>
      <div class="sub">OTHER SERVICES AVAILABLE!</div>
    </div>

    <div class="mascot" role="img" aria-label="Cartoon red lawn mower mascot with arms crossed"></div>

    <h1 class="company-name">Delbert n Db<br>Corporation<br>Lawn Care</h1>

    <div class="phone">407-555-0148</div>
    <div class="tagline">PROFFESSIONAL LAWN CARE SERVICES</div>
  </section>
</main>
</body>
</html>
```